Brightloom Business Card/Stationary
Marketing Co. Web/SEO
Brightloom Business Card/Stationary - Marketing
Creative Brief
Use specific fonts
Do your thing, logo is Trajan Pro and Tunga
Bright & Fun-filled
Reginald T. Ostrander
Senior SEO Consultant
www.brightloomxq.example
866-412-LOOM (5666)
855-390-LOOM (5666)
reggie@brightloomxq.example
I want this to be creative and memorable. We do web design, development and SEO. Make us stand out! I need business cards, stationary and envelop concepts.
I would like the back of the card to be the black logo with a corner peeled back slightly to reveal html code (to suggest what we do with website coding). If you don't know what that looks like right click a website and select view page source to get an idea.

```html
<!DOCTYPE html>
<html lang="en">
<head>
<meta charset="utf-8">
<title>Brightloom Business Card/Stationary</title>
<link rel="stylesheet" href="https://fonts.googleapis.com/css2?family=Cinzel:wght@600&family=Open+Sans:wght@400;600&display=swap">
<style>
:root{
  --navy:#14345a;
  --blue:#1f6fb0;
  --blue-light:#4fa3dc;
  --blue-dark:#0b2340;
  --grey:#9aa3ad;
  --grey-light:#dfe3e8;
  --ink:#333a42;
  --paper:#ffffff;
  --backdrop:#e9ecef;
  --black:#0c0d10;
}
*{box-sizing:border-box;margin:0;padding:0}
html,body{width:1200px;height:932px;overflow:hidden}
body{background:var(--backdrop);position:relative;font-family:"Open Sans",Arial,sans-serif;color:var(--ink)}
.piece{position:absolute;overflow:hidden;box-shadow:0 4px 14px rgba(0,0,0,.18)}
.piece > svg.art{position:absolute;inset:0;width:100%;height:100%}
.sheet{width:330px;height:466px;background:var(--paper);top:40px}
.fax-sheet{left:40px}
.letterhead{left:400px}
.brand{position:absolute;display:flex;align-items:center;gap:8px;white-space:nowrap}
.brand-dot{width:26px;height:26px;border-radius:50%;background:var(--navy);flex:none}
.brand-name{font-family:"Cinzel",Georgia,serif;font-weight:600;font-size:22px;color:var(--navy);letter-spacing:.5px}
.brand--light .brand-dot{background:#fff}
.brand--light .brand-name{color:#fff}
.sheet .brand-name{font-size:17px}
.sheet .brand-dot{width:22px;height:22px}
.faint-disc{position:absolute;border-radius:50%;background:var(--grey-light);opacity:.55}
.fax-sheet .brand{left:22px;top:62px}
.fax-title{position:absolute;left:22px;top:140px;font-size:30px;color:var(--ink);font-weight:400}
.fax-fields{position:absolute;left:22px;top:196px;width:210px;list-style:none}
.fax-fields li{font-size:10px;height:26px;border-bottom:1px solid var(--grey);padding-top:10px}
.fax-checks{position:absolute;left:22px;top:322px;display:flex;gap:26px;font-size:10px;list-style:none}
.fax-checks li::before{content:"";display:inline-block;width:8px;height:8px;border:1px solid var(--grey);margin-right:6px;vertical-align:-1px}
.letterhead .brand{left:22px;top:62px}
.contact{position:absolute;list-style:none;font-size:8.5px;line-height:14px;white-space:nowrap}
.contact li{display:flex;align-items:center;gap:5px}
.contact svg{width:8px;height:8px;fill:currentColor;flex:none}
.letterhead .contact{left:184px;top:58px;font-size:8px;line-height:13px;color:var(--ink)}
.envelope{left:40px;top:550px;width:690px;height:330px;background:var(--paper)}
.envelope .brand{left:40px;top:128px}
.envelope .brand-name{font-size:30px}
.envelope .brand-dot{width:34px;height:34px}
.flap-dot{position:absolute;left:333px;top:22px;width:24px;height:24px;border-radius:50%;background:var(--paper);opacity:.9}
.envelope-web{position:absolute;left:40px;top:278px;font-size:9px}
.card{width:380px;height:217px;left:780px}
.card-front{top:40px;background:linear-gradient(120deg,var(--blue-dark),var(--blue) 55%,var(--blue-light))}
.card-front .brand{left:22px;top:80px}
.card-front .brand-name{font-size:19px}
.card-name{position:absolute;right:22px;top:22px;text-align:right;color:#fff}
.card-name h2{font-size:13px;font-weight:600}
.card-name p{font-size:9px;opacity:.85}
.card-front .contact{right:22px;top:94px;color:#fff}
.card-back{top:290px;background:var(--black)}
.card-back .brand{left:96px;top:90px}
.card-back .brand-name{font-size:26px}
.card-peeled{top:540px;background:linear-gradient(135deg,#f4f5f7,#b9bfc6 60%,#e6e8eb)}
.card-peeled .brand{left:96px;top:90px}
.card-peeled .brand-name{font-size:26px}
.source-reveal{position:absolute;right:0;bottom:0;width:120px;height:90px;background:linear-gradient(135deg,#fff,#e7eef6);clip-path:polygon(100% 0,100% 100%,0 100%)}
.peel-flap{position:absolute;right:0;bottom:0;width:120px;height:90px;background:linear-gradient(135deg,#5a5e66,#16181c);clip-path:polygon(100% 0,0 100%,0 0)}
</style>
</head>
<body>

<section class="piece sheet fax-sheet" aria-label="Fax cover sheet">
  <svg class="art" viewBox="0 0 330 466" preserveAspectRatio="none" aria-hidden="true">
    <defs>
      <linearGradient id="bandFax" x1="0" y1="0" x2="1" y2="0"><stop offset="0" stop-color="#0b2340"/><stop offset="1" stop-color="#4fa3dc"/></linearGradient>
    </defs>
    <path d="M0 0H330V22C210 8 90 22 0 70Z" fill="url(#bandFax)"/>
    <path d="M0 80C90 30 210 18 330 30" stroke="#9aa3ad" stroke-width="3" fill="none"/>
    <path d="M330 390C250 430 160 450 60 466H330Z" fill="url(#bandFax)"/>
    <path d="M40 466C150 446 250 418 330 378" stroke="#9aa3ad" stroke-width="3" fill="none"/>
  </svg>
  <div class="faint-disc" style="left:200px;top:150px;width:110px;height:110px"></div>
  <div class="brand"><span class="brand-dot"></span><span class="brand-name">Brightloom</span></div>
  <h1 class="fax-title">FAX</h1>
  <ul class="fax-fields"><li>To :</li><li>Fax :</li><li>Phone :</li><li>Re :</li></ul>
  <ul class="fax-checks"><li>Urgent</li><li>For Review</li></ul>
</section>

<section class="piece sheet letterhead" aria-label="Letterhead">
  <svg class="art" viewBox="0 0 330 466" preserveAspectRatio="none" aria-hidden="true">
    <defs>
      <linearGradient id="bandLh" x1="0" y1="0" x2="1" y2="0"><stop offset="0" stop-color="#0b2340"/><stop offset="1" stop-color="#4fa3dc"/></linearGradient>
    </defs>
    <path d="M0 0H330V22C210 8 90 22 0 70Z" fill="url(#bandLh)"/>
    <path d="M0 80C90 30 210 18 330 30" stroke="#9aa3ad" stroke-width="3" fill="none"/>
    <path d="M330 390C250 430 160 450 60 466H330Z" fill="url(#bandLh)"/>
    <path d="M40 466C150 446 250 418 330 378" stroke="#9aa3ad" stroke-width="3" fill="none"/>
  </svg>
  <div class="faint-disc" style="left:200px;top:190px;width:110px;height:110px"></div>
  <div class="brand"><span class="brand-dot"></span><span class="brand-name">Brightloom</span></div>
  <ul class="contact">
    <li><svg viewBox="0 0 10 10"><path d="M2 0h2l1 3-1.5 1a6 6 0 0 0 2.5 2.5L7 5l3 1v2a2 2 0 0 1-2 2A8 8 0 0 1 0 2a2 2 0 0 1 2-2z"/></svg>866-412-LOOM (5666)</li>
    <li><svg viewBox="0 0 10 10"><path d="M2 0h2l1 3-1.5 1a6 6 0 0 0 2.5 2.5L7 5l3 1v2a2 2 0 0 1-2 2A8 8 0 0 1 0 2a2 2 0 0 1 2-2z"/></svg>855-390-LOOM (5666)</li>
    <li><svg viewBox="0 0 10 10"><path d="M0 2h10v6H0zM0 2l5 3 5-3" stroke="#fff" stroke-width=".8"/></svg>reggie@brightloomxq.example</li>
    <li><svg viewBox="0 0 10 10"><circle cx="5" cy="5" r="5"/></svg>www.brightloomxq.example</li>
  </ul>
</section>

<section class="piece envelope" aria-label="Envelope">
  <svg class="art" viewBox="0 0 690 330" preserveAspectRatio="none" aria-hidden="true">
    <defs>
      <linearGradient id="flap" x1="0" y1="0" x2="1" y2="0"><stop offset="0" stop-color="#0b2340"/><stop offset=".5" stop-color="#1f6fb0"/><stop offset="1" stop-color="#0b2340"/></linearGradient>
    </defs>
    <path d="M0 0H690V60C460 44 230 44 0 60Z" fill="url(#flap)"/>
    <path d="M0 70C230 54 460 54 690 70" stroke="#9aa3ad" stroke-width="3" fill="none"/>
    <path d="M690 230C600 290 500 318 400 330H690Z" fill="url(#flap)"/>
    <path d="M380 330C490 316 600 286 690 220" stroke="#9aa3ad" stroke-width="3" fill="none"/>
  </svg>
  <span class="flap-dot"></span>
  <div class="faint-disc" style="left:560px;top:120px;width:110px;height:110px"></div>
  <div class="brand"><span class="brand-dot"></span><span class="brand-name">Brightloom</span></div>
  <p class="envelope-web">www.brightloomxq.example</p>
</section>

<section class="piece card card-front" aria-label="Business card front">
  <svg class="art" viewBox="0 0 380 217" preserveAspectRatio="none" aria-hidden="true">
    <path d="M0 217C120 160 260 150 380 170V217Z" fill="#ffffff" opacity=".15"/>
    <path d="M0 200C120 148 260 140 380 160" stroke="#dfe3e8" stroke-width="2" fill="none"/>
  </svg>
  <div class="brand brand--light"><span class="brand-dot"></span><span class="brand-name">Brightloom</span></div>
  <div class="card-name"><h2>Reginald T. Ostrander</h2><p>Senior SEO Consultant</p></div>
  <ul class="contact">
    <li>866-412-LOOM (5666)</li>
    <li>855-390-LOOM (5666)</li>
    <li>reggie@brightloomxq.example</li>
    <li>www.brightloomxq.example</li>
  </ul>
</section>

<section class="piece card card-back" aria-label="Business card back">
  <svg class="art" viewBox="0 0 380 217" preserveAspectRatio="none" aria-hidden="true">
    <path d="M0 0H160C100 20 40 50 0 90Z" fill="#1f6fb0" opacity=".5"/>
    <path d="M380 217H220C280 197 340 167 380 127Z" fill="#1f6fb0" opacity=".5"/>
  </svg>
  <div class="brand brand--light"><span class="brand-dot"></span><span class="brand-name">Brightloom</span></div>
</section>

<section class="piece card card-peeled" aria-label="Business card back with peeled corner">
  <div class="brand"><span class="brand-dot"></span><span class="brand-name">Brightloom</span></div>
  <div class="source-reveal" role="img" aria-label="Web page source code revealed under the peeled corner"></div>
  <div class="peel-flap"></div>
</section>

</body>
</html>
```